hand painted address sign/ old golf course look

i would like a design a golf course sign that would include my address
This project is an address sign for the front of my house, personal residence.
The design specifics are to include my address, 417 Brenton Rd. I would like the the address to be written in a script font. The colors are white and green and maybe some gold. I am also looking for a silhouette of a sycamore tree. The size of the design should be 24”high x 20”wide. The shape of the design should be like a shield or badge shape. The attached photo shows the shapes i am interested in S1, S8.
I love golf and i envision my address sign imitates an old classic traditional golf club.

```html
<!DOCTYPE html>
<html lang="en">
<head>
<meta charset="UTF-8">
<title>417 Brenton Rd. – Address Sign</title>
<link rel="stylesheet" href="https://fonts.googleapis.com/css2?family=Caveat+Brush&display=swap">
<style>
  :root {
    --backdrop: #f3f2ec;
    --sign-green: #a9c862;
    --sign-white: #f8faf0;
    --tree-tone: #eef3e0;
  }
  html, body {
    margin: 0;
    padding: 0;
    overflow: hidden;
  }
  .canvas {
    position: relative;
    width: 1085px;
    height: 1200px;
    background: var(--backdrop);
    overflow: hidden;
  }
  .address-sign {
    position: absolute;
    left: 102px;
    top: 76px;
    width: 880px;
    height: 1048px;
  }
  .address-sign__shape {
    position: absolute;
    inset: 0;
    width: 100%;
    height: 100%;
  }
  .address-sign__field { fill: var(--sign-green); }
  .address-sign__border {
    fill: none;
    stroke: var(--sign-white);
    stroke-width: 6;
    stroke-linejoin: round;
  }
  .address-sign__tree { fill: var(--tree-tone); }
  .address-sign__star { fill: var(--sign-white); }
  .address-sign__address {
    position: absolute;
    left: 0;
    right: 0;
    top: 612px;
    margin: 0;
    text-align: center;
    font-family: "Caveat Brush", cursive;
    font-weight: 400;
    font-size: 112px;
    line-height: 1;
    letter-spacing: 2px;
    color: var(--sign-white);
  }
</style>
</head>
<body>
  <main class="canvas">
    <section class="address-sign">
      <svg class="address-sign__shape" viewBox="0 0 880 1048" xmlns="http://www.w3.org/2000/svg">
        <defs>
          <polygon id="star" points="0,-1 0.2245,-0.309 0.951,-0.309 0.363,0.118 0.588,0.809 0,0.382 -0.588,0.809 -0.363,0.118 -0.951,-0.309 -0.2245,-0.309"/>
        </defs>
        <path class="address-sign__field" d="M0,0 H880 V800 L440,1048 L0,800 Z"/>
        <path class="address-sign__border" d="M24,24 H856 V784 L440,1018 L24,784 Z"/>
        <rect class="address-sign__tree" x="284" y="117" width="340" height="400" rx="120"
              role="img" aria-label="White silhouette of a sycamore tree with a broad rounded crown"/>
        <g class="address-sign__stars">
          <use href="#star" class="address-sign__star" transform="translate(318 872) scale(32)"/>
          <use href="#star" class="address-sign__star" transform="translate(440 878) scale(42)"/>
          <use href="#star" class="address-sign__star" transform="translate(562 872) scale(32)"/>
        </g>
      </svg>
      <p class="address-sign__address">417 Brenton Rd.</p>
    </section>
  </main>
</body>
</html>
```